Spring Camp flyer

I would like a postcard that promotes our Spring Break Camp, with normal postcard design on reverse side. The target age group for our camp is between 2 and 7 years old, it needs to be very visually appealing and exciting! Vibrant and quite cool so that people want to pick it up and see what it is :)
I love the file titled SpringBrk a lot!
I also need the details
www.zelvanoro.ae
info@zelvanoro.ae
Camp is 800 aed per week
1200 for both weeks
9am - 2pm with early drop and late pick up available
Um Suqeim 3 location
Daily activities include;
yoga, brain training, language, creative arts, sports and more!
Online gallery updated daily!

```html
<!DOCTYPE html>
<html lang="en">
<head>
<meta charset="utf-8">
<title>Spring Camp Flyer</title>
<link rel="stylesheet" href="https://fonts.googleapis.com/css2?family=Patrick+Hand&display=swap">
<style>
  :root {
    --coral: #f2897a;
    --peach: #f6b9a0;
    --mint: #8fd3c1;
    --plum: #8a6d92;
    --sun: #f5c64b;
    --berry: #d8423c;
    --ink: #2a2a2a;
    --paper: #ffffff;
    --leaf: #bfe6d6;
  }
  * { margin: 0; padding: 0; box-sizing: border-box; }
  html, body { width: 1200px; height: 929px; overflow: hidden; background: var(--paper); }
  .flyer {
    position: relative;
    width: 1200px; height: 929px;
    font-family: "Patrick Hand", "Comic Sans MS", cursive;
    color: var(--ink);
    overflow: hidden;
  }
  .pattern-field {
    position: absolute; inset: 0;
    background: linear-gradient(160deg, var(--mint) 0%, var(--peach) 30%, var(--coral) 55%, var(--plum) 80%, var(--mint) 100%);
  }
  .blank-panel {
    position: absolute; left: 580px; top: 372px; width: 620px; height: 557px;
    background: var(--paper);
  }
  .info-card { position: absolute; left: 65px; top: 165px; width: 515px; height: 720px; }
  .info-card svg { position: absolute; inset: 0; }
  .wreath {
    position: absolute; left: 120px; top: 360px; width: 400px; height: 290px;
    border-radius: 50%;
    background: radial-gradient(ellipse at center, transparent 52%, var(--leaf) 54%, transparent 72%);
    opacity: .8;
  }
  .songbird-yellow {
    position: absolute; left: 110px; top: 320px; width: 120px; height: 80px;
    border-radius: 50% 40% 50% 50%;
    background: var(--sun);
  }
  .songbird-plum {
    position: absolute; left: 400px; top: 70px; width: 110px; height: 80px;
    border-radius: 50% 40% 50% 50%;
    background: var(--plum);
  }
  .card-text {
    position: absolute; left: 65px; top: 165px; width: 515px;
    text-align: center; font-size: 32px; line-height: 1;
  }
  .card-text p { position: absolute; left: 0; width: 100%; }
  .age-badge { position: absolute; left: 565px; top: -45px; width: 360px; height: 360px; }
  .badge-text {
    position: absolute; left: 565px; top: -45px; width: 360px; height: 360px;
    color: var(--paper); text-align: center;
    transform: rotate(-16deg);
    display: flex; flex-direction: column; justify-content: center; align-items: center;
    padding-top: 20px;
  }
  .badge-text .ages { font-size: 56px; line-height: 1.05; }
  .badge-text .note { font-size: 36px; line-height: 1.15; }
</style>
</head>
<body>
<main class="flyer">
  <div class="pattern-field" role="img" aria-label="Colourful chevron stripe pattern in coral, mint and plum"></div>
  <div class="blank-panel"></div>

  <div class="info-card">
    <svg width="515" height="720" viewBox="0 0 515 720">
      <path d="M40 4 H475 A36 36 0 0 0 511 40 V680 A36 36 0 0 0 475 716 H40 A36 36 0 0 0 4 680 V40 A36 36 0 0 0 40 4 Z"
            fill="var(--paper)" stroke="var(--berry)" stroke-width="6"/>
    </svg>
  </div>
  <div class="wreath" role="img" aria-label="Soft green leafy wreath framing the prices"></div>
  <div class="songbird-yellow" role="img" aria-label="Small yellow songbird illustration"></div>

  <div class="card-text">
    <p style="top:52px">Daily activities include:</p>
    <p style="top:96px">Yoga</p>
    <p style="top:135px">Brain Training</p>
    <p style="top:174px">Language</p>
    <p style="top:213px">Creative Arts</p>
    <p style="top:252px">Sports &amp; More!</p>
    <p style="top:305px">800 AED per week</p>
    <p style="top:337px;font-size:26px">or</p>
    <p style="top:364px">1200 AED for both weeks</p>
    <p style="top:421px">Umm Suqeim 3 Locations</p>
    <p style="top:481px">9am - 2pm</p>
    <p style="top:517px">early drop &amp;</p>
    <p style="top:550px">late pick up available</p>
    <p style="top:624px">www.zelvanoro.ae</p>
    <p style="top:663px">info@zelvanoro.ae</p>
  </div>

  <svg class="age-badge" viewBox="0 0 360 360">
    <circle cx="180" cy="180" r="150" fill="var(--sun)" stroke="var(--sun)" stroke-width="26"
            stroke-dasharray="0 27" stroke-linecap="round"/>
    <circle cx="180" cy="180" r="128" fill="none" stroke="var(--paper)" stroke-width="3"/>
  </svg>
  <div class="badge-text">
    <span class="ages">Ages 2-7</span>
    <span class="note">Online Gallery</span>
    <span class="note">Updated Daily!</span>
  </div>
  <div class="songbird-plum" role="img" aria-label="Small plum songbird illustration perched on the badge"></div>
</main>
</body>
</html>
```